Figure for Manufacture of Wound Healing Gel

Who we are: We are a nationally funded bioengineering laboratory at Harlow Ridge University conducting research on the tendon healing properties of a gel manufactured from real tendon.

What we need: We require a figure piece that will be included in an academic publication. With that in mind, the figure must be professional, clear, and concise. A reader would need to glance at the figure for only a moment to understand the process of how we manufacture and store tendon gel. Actual pictures of the in-between steps are included and will need to be cropped to improve the professional look of the design.

The Details: The figure should stepwise show the process of how we manufacture and store tendon gel. In brief, we harvest tendon from donor cadavers. Those tendons undergo decellularization, lyophilization (fancy word for freeze-drying), and are milled into a fine powder. The powder is set in acidified water and treated with digestive enzymes. After 24 hrs, the gel is brought to physiologic pH and salinity and placed in vials. The vials are frozen and again lyophilized (this is so they can be stored and transported easily). Finally the samples are reconstituted with DI water.

The Figure: Should be a linear process (horizontal). The following are the actual steps we wish to include (steps need not be numbered necessarily as long as they are in logical order...

1.) A picture of harvested tendon (Step 1.jpg)
2.) Written description: "Decellularization, lyophilization, and milling"
3.) A picture of milled tendon powder (Step 2.jpg)
4.) Written description: "Digestion with pepsin before establishing physiologic pH and salinity".
5.) A picture of gel (Step 3.jpg)
6.) Written description: "Lyophilization of aliquots"
7.) A picture of freeze-dried gel (Step 4.jpg)
8.) Written description: "Reconstitution with DI water"
9.) A picture of reconstituted gel (Step 5.jpg)

Feel free to message for any questions, comments, or clarifications.

```html
<!DOCTYPE html>
<html lang="en">
<head>
<meta charset="utf-8">
<title>Tendon Gel Manufacture Process Figure</title>
<link rel="stylesheet" href="https://fonts.googleapis.com/css2?family=Roboto+Condensed:wght@400;700&display=swap">
<style>
  :root {
    --paper: #ffffff;
    --flow-band: #c8c8c8;
    --arrow-head: #bdbdbd;
    --ink: #1c1c1c;
    --caption-ink: #555555;
    --dish-edge: #f4f4f4;
    --tendon: #d9cba9;
    --powder: #ece3b6;
    --gel: #d3d8d8;
    --glass: #eeeeee;
    --gel-liquid: #d6cbb2;
    --dried-gel: #e6e2da;
  }
  html, body {
    margin: 0;
    padding: 0;
    width: 1200px;
    height: 272px;
    overflow: hidden;
    background: var(--paper);
  }
  .process-figure {
    display: block;
    width: 1200px;
    height: 272px;
  }
  .flow-band { fill: var(--flow-band); }
  .flow-arrow { fill: var(--arrow-head); }
  .step-label {
    font-family: "Roboto Condensed", "Arial Narrow", sans-serif;
    font-weight: 700;
    font-size: 10px;
    letter-spacing: 0.8px;
    fill: var(--ink);
    text-anchor: middle;
  }
  .figure-caption {
    font-family: "Roboto Condensed", "Arial Narrow", sans-serif;
    font-weight: 400;
    font-size: 7px;
    letter-spacing: 0.6px;
    fill: var(--caption-ink);
    text-anchor: middle;
  }
</style>
</head>
<body>
<svg class="process-figure" viewBox="0 0 1200 272" xmlns="http://www.w3.org/2000/svg">
  <defs>
    <radialGradient id="dish-tendon-tone" cx="0.5" cy="0.45" r="0.5">
      <stop offset="0" stop-color="var(--tendon)"/>
      <stop offset="0.55" stop-color="#ece5d4"/>
      <stop offset="1" stop-color="var(--dish-edge)"/>
    </radialGradient>
    <radialGradient id="dish-powder-tone" cx="0.5" cy="0.45" r="0.5">
      <stop offset="0" stop-color="var(--powder)"/>
      <stop offset="0.5" stop-color="#f3eed4"/>
      <stop offset="1" stop-color="var(--dish-edge)"/>
    </radialGradient>
    <radialGradient id="dish-gel-tone" cx="0.5" cy="0.45" r="0.5">
      <stop offset="0" stop-color="var(--gel)"/>
      <stop offset="0.5" stop-color="#e6e8e8"/>
      <stop offset="1" stop-color="var(--dish-edge)"/>
    </radialGradient>
    <linearGradient id="vial-lyophilized-tone" x1="0" y1="0" x2="0" y2="1">
      <stop offset="0" stop-color="var(--glass)"/>
      <stop offset="0.46" stop-color="var(--glass)"/>
      <stop offset="0.52" stop-color="var(--gel-liquid)"/>
      <stop offset="1" stop-color="var(--gel-liquid)"/>
    </linearGradient>
    <linearGradient id="vial-reconstituted-tone" x1="0" y1="0" x2="0" y2="1">
      <stop offset="0" stop-color="var(--glass)"/>
      <stop offset="0.72" stop-color="var(--glass)"/>
      <stop offset="0.8" stop-color="var(--dried-gel)"/>
      <stop offset="1" stop-color="#ddd8cf"/>
    </linearGradient>
  </defs>

  <!-- process flow band and final arrow -->
  <rect class="flow-band" x="220" y="118" width="780" height="28"/>
  <polygon class="flow-arrow" points="995,72 1050,72 1050,14 1115,132 1050,250 1050,194 995,194"/>

  <!-- step images -->
  <ellipse role="img" aria-label="Dish of harvested tendon strands" cx="118" cy="148" rx="100" ry="78" fill="url(#dish-tendon-tone)"/>
  <ellipse role="img" aria-label="Dish of milled tendon powder" cx="399" cy="146" rx="100" ry="78" fill="url(#dish-powder-tone)"/>
  <ellipse role="img" aria-label="Dish of tendon hydrogel" cx="724" cy="146" rx="96" ry="76" fill="url(#dish-gel-tone)"/>
  <rect role="img" aria-label="Vial of freeze-dried hydrogel" x="945" y="45" width="43" height="207" rx="3" fill="url(#vial-lyophilized-tone)"/>
  <rect role="img" aria-label="Vial of hydrogel reconstituted with DI water" x="1130" y="45" width="43" height="207" rx="3" fill="url(#vial-reconstituted-tone)"/>

  <!-- step labels -->
  <text class="step-label" y="176">
    <tspan x="266">DECELLULARIZED,</tspan>
    <tspan x="266" dy="14">LYOPHILIZED,</tspan>
    <tspan x="266" dy="14">AND MILLED</tspan>
  </text>
  <text class="step-label" y="176">
    <tspan x="566">DIGESTED AND</tspan>
    <tspan x="566" dy="14">BROUGHT TO</tspan>
    <tspan x="566" dy="14">PHYSIOLOGIC pH AND SALINITY</tspan>
  </text>
  <text class="step-label" y="176">
    <tspan x="868">HYDROGEL</tspan>
    <tspan x="868" dy="14">LYOPHILIZED</tspan>
  </text>
  <text class="step-label" y="176">
    <tspan x="1042">RECONSTITUTED</tspan>
    <tspan x="1042" dy="14">WITH DI WATER</tspan>
  </text>

  <text class="figure-caption" x="620" y="248">FIGURE (VERSION) 5</text>
</svg>
</body>
</html>
```